Pelton Mortgage Capital Business Card

We need a business card design for our mortgage servicing company. In addition to servicing the loans of homeowners, we help homeowners with purchasing their homes and any mortgage refinancing. We would like to see designs that use the colors in the logo attached below (gold-ish yellow and navy blue), and any other design you deem fit! The design should communicate a simpler life with smart mortgages provided by Pelton.

```html
<!DOCTYPE html>
<html lang="en">
<head>
<meta charset="utf-8">
<title>Pelton Mortgage Capital — Business Card</title>
<link href="https://fonts.googleapis.com/css2?family=Montserrat:wght@400;500;700&display=swap" rel="stylesheet">
<style>
  :root {
    --navy: #262052;
    --gold: #e2b23c;
    --white: #ffffff;
    --backdrop: #2a2a2c;
  }
  * { box-sizing: border-box; margin: 0; padding: 0; }
  html, body {
    width: 1200px; height: 880px; overflow: hidden;
    background: var(--backdrop);
    font-family: "Montserrat", sans-serif;
  }
  .canvas { position: relative; width: 1200px; height: 880px; }
  .card {
    position: absolute; width: 700px; height: 400px; overflow: hidden;
    box-shadow: 0 14px 30px rgba(0,0,0,.45);
  }
  .card-front { left: 60px; top: 30px; background: var(--navy); }
  .card-back { left: 440px; top: 450px; background: var(--white); }

  .wordmark {
    position: absolute; font-weight: 700; line-height: 1; white-space: nowrap;
    display: flex; align-items: center; gap: 14px;
  }
  .wordmark-dot { border-radius: 50%; flex: none; }
  .card-front .wordmark {
    left: 50%; top: 50%; transform: translate(-50%, -50%);
    color: var(--gold); font-size: 64px;
  }
  .card-front .wordmark-dot { width: 30px; height: 30px; background: var(--gold); }
  .card-back .wordmark {
    left: 70px; top: 120px; color: var(--navy); font-size: 32px;
  }
  .card-back .wordmark-dot { width: 16px; height: 16px; background: var(--navy); }

  .wave { position: absolute; inset: 0; }

  .contact {
    position: absolute; right: 40px; top: 128px; text-align: right;
    color: var(--white);
  }
  .contact-name { font-weight: 700; font-size: 21px; letter-spacing: .5px; }
  .contact-role { font-size: 14px; margin-top: 4px; }
  .contact-address { font-size: 14px; line-height: 1.45; margin-top: 22px; }
  .contact-lines { list-style: none; margin-top: 18px; font-size: 14px; }
  .contact-lines li {
    display: flex; justify-content: flex-end; align-items: center;
    gap: 10px; height: 26px;
  }
  .contact-lines svg { width: 16px; height: 16px; fill: var(--gold); flex: none; }
</style>
</head>
<body>
<div class="canvas">

  <section class="card card-front">
    <div class="wordmark"><span class="wordmark-dot"></span>Pelton Mortgage</div>
  </section>

  <section class="card card-back">
    <svg class="wave" viewBox="0 0 700 400" preserveAspectRatio="none" aria-hidden="true">
      <path fill="#262052" d="M0,308 C200,298 300,268 380,188 C460,98 520,8 700,-2 L700,400 L0,400 Z"/>
      <path fill="#ffffff" d="M0,314 C200,304 300,274 380,194 C460,104 520,14 700,4 L700,400 L0,400 Z"/>
      <path fill="#e2b23c" d="M0,322 C200,312 300,282 380,202 C460,112 520,22 700,12 L700,400 L0,400 Z"/>
      <path fill="#ffffff" d="M0,342 C200,332 300,302 380,222 C460,132 520,42 700,32 L700,400 L0,400 Z"/>
      <path fill="#262052" d="M0,346 C200,336 300,306 380,226 C460,136 520,46 700,36 L700,400 L0,400 Z"/>
    </svg>

    <div class="wordmark"><span class="wordmark-dot"></span>Pelton Mortgage</div>

    <div class="contact">
      <p class="contact-name">DARIN HOLLOWAY</p>
      <p class="contact-role">Owner</p>
      <p class="contact-address">2710 Lindell Ave, Ste<br>200, Dallas, TX 75204</p>
      <ul class="contact-lines">
        <li>214.555.0186
          <svg viewBox="0 0 24 24" aria-hidden="true"><path d="M6.6 10.8a15 15 0 0 0 6.6 6.6l2.2-2.2a1 1 0 0 1 1-.25 11.4 11.4 0 0 0 3.6.57 1 1 0 0 1 1 1V20a1 1 0 0 1-1 1A17 17 0 0 1 3 4a1 1 0 0 1 1-1h3.5a1 1 0 0 1 1 1c0 1.25.2 2.45.57 3.57a1 1 0 0 1-.25 1z"/></svg>
        </li>
        <li>info@peltonmortgage.com
          <svg viewBox="0 0 24 24" aria-hidden="true"><path d="M2 5h20v14H2z M2 5l10 8 10-8" stroke="#262052" stroke-width="1.5"/></svg>
        </li>
        <li>www.peltonmortgage.com
          <svg viewBox="0 0 24 24" aria-hidden="true"><circle cx="12" cy="12" r="10"/><path d="M2 12h20M12 2c3 3 3 17 0 20M12 2c-3 3-3 17 0 20" stroke="#262052" stroke-width="1.3" fill="none"/></svg>
        </li>
      </ul>
    </div>
  </section>

</div>
</body>
</html>
```